EPC Marketing Flyer Pinefold HC

Company Name: Pinefold Homecheck Ltd
Product: Residential EPCs
Territory: Nationwide (UK)
Marketing channel: Flyer will be used for email and postal mailshots. We have not targeted this particular segment of the market before, so we need it to be eye catching, clearly messaged and encourage the recipient to get in touch.

We need a flyer to promote our services to conduct EPCs owned by public and private sector for residential ONLY (NOT Commercial), on a large or small scale.

Our Surveyors: experienced and accredited surveyors, quality service, quick and professional

Our Business: Warm Ledger Accredited, Reputation in business for excellence, fast growing

Our Service: Friendly, high quality, quick and professional

Colours: Designs in green and white (same shade as corporate colours), with our logo, and warm ledger accreditation logo, promoting our business.

Target Market(s)

Estate Agencies, Housing Associations, Local Authorities (Housing Departments), House Builders (NOT Home Owners Directly)

Industry/Entity Type

It Company

Font styles to use
Sans Serif
Other font styles liked:
• Calibri

Colors
add136
9bcb3c
cadf82
f6faec
eaf2ce

Requirements
Must have
• Our contact number etc must be clearly visible, and that we do EPCs
• Must state: What is an EPC? An EPC (Energy Performance Certificate) gives a property an energy efficiency rating from A (most efficient) to G (least efficient) and is valid for 10 years. An EPC can also provide recommendations on home improvement measures which once complete can improve the energy efficiency of the property.
• Who needs and EPC? All landlords and home owners, as all properties available to buy or rent require a valid and current EPC.
• Contact details:
• Tel: 08000 915 462
• Website: www.pinefold-hc.co.uk
• Email: epc@pinefold-hc.co.uk
• we must also be ably to print out the flyer
Nice to have
• Nice images to accompany the text which give a feeling of Environmentally Green, Home Energy Efficiency, Home Warmth and family - see example attached. And image of survey professional at work.
Should not have
• Any reference to cost or pricing
• Warm ledger logo art work must not be any other size that that specified in guidance document attached.

```html
<!DOCTYPE html>
<html lang="en">
<head>
<meta charset="utf-8">
<title>We Do EPCs – Pinefold Homecheck Ltd</title>
<link rel="stylesheet" href="https://fonts.googleapis.com/css2?family=Arimo:wght@400;700&display=swap">
<style>
  :root {
    --green: #9bcb3c;
    --green-pale: #cadf82;
    --badge: #4d7d2c;
    --ink: #1e3313;
    --ink-soft: #2a2a2a;
    --white: #ffffff;
    --sky-top: #5d9fd8;
    --sky-mid: #cfe3f4;
    --warm: #d8b48f;
    --grass: #8fc04a;
  }
  * { margin: 0; padding: 0; box-sizing: border-box; }
  html, body { width: 1200px; height: 851px; overflow: hidden; background: var(--white); }
  body { font-family: "Arimo", Arial, sans-serif; }
  .flyer { position: relative; width: 1200px; height: 851px; overflow: hidden; background: var(--white); }
  .flyer__shapes { position: absolute; inset: 0; }

  .brand {
    position: absolute; left: 58px; top: 128px;
    display: flex; align-items: center; gap: 18px;
  }
  .brand__dot { width: 78px; height: 78px; border-radius: 50%; background: var(--green); }
  .brand__name { font-weight: 700; font-size: 34px; line-height: 1.1; color: var(--ink); }

  .headline {
    position: absolute; left: 44px; top: 440px;
    font-size: 67px; line-height: 1; font-weight: 700; color: var(--ink); letter-spacing: -0.3px;
  }
  .info { position: absolute; left: 48px; width: 480px; color: var(--white); }
  .info__title { font-size: 22px; line-height: 1.2; font-weight: 700; letter-spacing: 0.3px; margin-bottom: 9px; }
  .info__lead { font-size: 18.5px; line-height: 1.2; color: var(--ink-soft); letter-spacing: 0.6px; margin-bottom: 3px; }
  .info__body { font-size: 14.8px; line-height: 21px; letter-spacing: 0.55px; }
  .info--what { top: 518px; }
  .info--who { top: 700px; }

  .contact {
    position: absolute; left: 672px; top: 692px; list-style: none;
    color: var(--white); font-size: 29px; letter-spacing: 1.4px;
  }
  .contact__item { display: flex; align-items: center; gap: 16px; height: 39px; }
  .contact__icon { width: 28px; height: 28px; flex: none; }
</style>
</head>
<body>
<div class="flyer">
  <svg class="flyer__shapes" width="1200" height="851" viewBox="0 0 1200 851">
    <defs>
      <linearGradient id="photoTone" x1="0" y1="0" x2="0" y2="1">
        <stop offset="0" stop-color="var(--sky-top)"/>
        <stop offset="0.42" stop-color="var(--sky-mid)"/>
        <stop offset="0.72" stop-color="var(--warm)"/>
        <stop offset="1" stop-color="var(--grass)"/>
      </linearGradient>
      <radialGradient id="photoGlow" cx="0.62" cy="0.62" r="0.5">
        <stop offset="0" stop-color="#e9c9a3" stop-opacity="0.85"/>
        <stop offset="1" stop-color="#e9c9a3" stop-opacity="0"/>
      </radialGradient>
    </defs>
    <path class="band-green" fill="var(--green)"
      d="M0,334 C240,300 470,350 640,470 C790,575 910,650 1020,655 C1110,658 1165,640 1200,625 L1200,851 L0,851 Z"/>
    <g class="photo" role="img"
      aria-label="Photo: smiling family lying on grass in front of a pale green house outline under a blue cloudy sky">
      <path fill="url(#photoTone)" stroke="var(--white)" stroke-width="14"
        d="M525,-10 L1210,-10 L1210,595 C1100,662 900,680 760,612 C600,530 505,390 502,250 C500,150 510,60 525,-10 Z"/>
      <path fill="url(#photoGlow)"
        d="M525,-10 L1210,-10 L1210,595 C1100,662 900,680 760,612 C600,530 505,390 502,250 C500,150 510,60 525,-10 Z"/>
    </g>
    <rect class="badge" x="1013" y="44" width="122" height="156" rx="6" fill="var(--badge)" opacity="0.85"/>
  </svg>

  <div class="brand">
    <span class="brand__dot"></span>
    <span class="brand__name">Pinefold<br>Homecheck Ltd</span>
  </div>

  <h1 class="headline">We Do EPCs</h1>

  <section class="info info--what">
    <h2 class="info__title">What is an EPC?</h2>
    <p class="info__lead">An EPC (Energy Performance Certificate)</p>
    <p class="info__body">gives a property an energy efficiency rating from A (most efficient) to G (least efficient) and is valid for 10 years. An EPC can also provide recommendations on home improvement measures which once complete can improve the energy efficiency of the property.</p>
  </section>

  <section class="info info--who">
    <h2 class="info__title">Who needs and EPC?</h2>
    <p class="info__lead">All landlords and home owners,</p>
    <p class="info__body">as all properties available to buy or rent require a valid and current EPC.</p>
  </section>

  <ul class="contact">
    <li class="contact__item">
      <svg class="contact__icon" viewBox="0 0 28 28" aria-hidden="true">
        <path fill="var(--ink)" d="M3,9 C3,5 8,3 14,3 C20,3 25,5 25,9 L25,11 L19,11 L19,8 L9,8 L9,11 L3,11 Z"/>
        <path fill="var(--ink)" d="M7,12 L21,12 L25,24 L3,24 Z"/>
        <circle cx="14" cy="18" r="3.5" fill="var(--green)"/>
      </svg>
      <span>08000 915 462</span>
    </li>
    <li class="contact__item">
      <svg class="contact__icon" viewBox="0 0 28 28" aria-hidden="true">
        <rect x="2" y="6" width="24" height="17" fill="var(--ink)"/>
        <path d="M3,7 L14,16 L25,7" fill="none" stroke="var(--green)" stroke-width="2"/>
      </svg>
      <span>epc@pinefold-hc.co.uk</span>
    </li>
    <li class="contact__item">
      <svg class="contact__icon" viewBox="0 0 28 28" aria-hidden="true">
        <g fill="none" stroke="var(--ink)" stroke-width="2.4">
          <circle cx="14" cy="14" r="11"/>
          <ellipse cx="14" cy="14" rx="5" ry="11"/>
          <path d="M3,14 L25,14 M5,8 L23,8 M5,20 L23,20"/>
        </g>
      </svg>
      <span>www.pinefold-hc.co.uk</span>
    </li>
  </ul>
</div>
</body>
</html>
```